Web Design Project

We are looking for a beautiful, clean web page design for our new web service: Tavernik. The idea behind tavernik is simple. People tell us where they live and what they love, and we point them towards interesting offers, places and events near them - as reviewed by our experts and their friends. It is available on the web and by phone. We have chosen our logo and know the elements we want on each page. Now we just need a whole a great design to pull it all together.
///
TaVernik
locate, explore and discover the best of your city with tavernik
Discover your cities hottest offers
places & venues while sharing
the things that mean the most to you.
Join for free today!
//
Note: we have also had some feedback that the name is difficult to read/pronounce, so we might want to change the color of the word be in tavernik so that it stands out. suggestions welcome.
Target Market(s)
Young, urban, savvy consumers
We are looking at this site for inspiration
https://strovento.example/
elements: blog:latest news, top picks // members area // categories: fashion & beauty; food & drink; entertainment & events

```html
<!DOCTYPE html>
<html lang="en">
<head>
<meta charset="utf-8">
<title>Tavernik – Locate, Explore and Discover</title>
<link rel="stylesheet" href="https://fonts.googleapis.com/css2?family=Arimo:wght@400;700&family=PT+Sans:wght@400;700&display=swap">
<style>
  :root {
    --sky-top: #3f8fd0;
    --sky-mid: #8ec3ea;
    --sky-low: #d6ebf8;
    --page-bg: #efefef;
    --panel-blue: #6eaedd;
    --panel-edge: #4f93c8;
    --white: #ffffff;
    --ink: #222222;
    --ink-soft: #444444;
    --link-blue: #2c8fd0;
    --tab-green: #1a9a5c;
    --tab-green-dark: #0d7a44;
    --tab-cyan: #bfe9ee;
    --bar-top: #a8d4f2;
    --bar-bottom: #5fa7dc;
    --field-bg: #e9e9e9;
    --field-line: #b9b9b9;
    --badge-blue: #2f7fc4;
    --logo-ink: #555555;
    --logo-mark: #6a3aa0;
  }
  * { box-sizing: border-box; margin: 0; padding: 0; }
  html, body { width: 905px; height: 1200px; overflow: hidden; }
  body {
    position: relative;
    background: var(--page-bg);
    font-family: "Arimo", Arial, sans-serif;
    color: var(--ink);
  }
  .abs { position: absolute; }

  /* header */
  .sky {
    left: 0; top: 0; width: 905px; height: 375px;
    background: linear-gradient(180deg, var(--sky-top) 0%, var(--sky-mid) 45%, var(--sky-low) 100%);
  }
  .brand { left: 22px; top: 30px; display: flex; align-items: center; gap: 10px; }
  .brand-mark { width: 34px; height: 34px; background: var(--logo-mark); }
  .brand-name {
    font-family: "PT Sans", sans-serif; font-size: 40px; font-weight: 400;
    color: var(--logo-ink); letter-spacing: 1px; line-height: 1; margin-top: 60px;
  }
  .brand { top: 20px; align-items: flex-end; }
  .brand-mark { margin-bottom: 6px; }
  .tagline { left: 241px; top: 67px; font-size: 15px; color: #111; }

  .nav { top: 120px; height: 31px; font-size: 12px; display: flex; align-items: center; justify-content: center;
    border-radius: 4px 4px 0 0; color: #113; }
  .nav-home { left: 620px; width: 81px; background: linear-gradient(var(--tab-green), var(--tab-green-dark)); color: var(--white); }
  .nav-about { left: 706px; width: 80px; background: linear-gradient(#e6fbfd, var(--tab-cyan)); }
  .nav-contact { left: 790px; width: 82px; background: linear-gradient(#e6fbfd, var(--tab-cyan)); }

  /* slider */
  .slider {
    left: 15px; top: 151px; width: 873px; height: 362px;
    background: var(--panel-blue); border-radius: 4px;
    box-shadow: 0 6px 8px rgba(0,0,0,0.18);
  }
  .slide { top: 165px; width: 271px; height: 336px; background: var(--white); border-radius: 4px; padding: 5px; }
  .slide-photo { width: 100%; height: 100%; border-radius: 3px; position: relative; }
  .slide-title { position: absolute; top: 10px; left: 0; right: 0; text-align: center; font-size: 22px; }
  .slide-cta { position: absolute; right: 8px; bottom: 8px; font-size: 16px; }
  .slide-beauty { left: 34px; }
  .slide-beauty .slide-photo { background: linear-gradient(180deg, #3f8fd6 0%, #9ccbee 40%, #3bbfc8 65%, #bfe1d5 100%); }
  .slide-food { left: 316px; }
  .slide-food .slide-photo { background: linear-gradient(180deg, #d9c89a 0%, #efe6cf 50%, #e2c060 80%, #f2ecdc 100%); }
  .slide-theatre { left: 597px; }
  .slide-theatre .slide-photo { background: linear-gradient(180deg, #c8a6b8 0%, #7a4056 40%, #3a1420 60%, #a8323a 100%); }
  .slide-theatre .slide-title, .slide-theatre .slide-cta { color: var(--white); }
  .slider-arrow { top: 301px; width: 28px; height: 48px; background: var(--white); }
  .slider-arrow svg { position: absolute; top: 17px; }
  .arrow-left { left: 15px; border-radius: 0 24px 24px 0; }
  .arrow-left svg { left: 3px; }
  .arrow-right { left: 860px; border-radius: 24px 0 0 24px; }
  .arrow-right svg { left: 10px; }

  /* boxes */
  .box { background: var(--white); border-radius: 4px; }
  .box-heading { font-family: "PT Sans", sans-serif; font-size: 16px; color: var(--ink); text-transform: uppercase; }
  .link-more { font-size: 11px; color: var(--link-blue); }

  .intro { left: 27px; top: 553px; width: 580px; height: 121px; }
  .intro-copy { left: 59px; top: 578px; font-family: "PT Sans", sans-serif; font-size: 16px; line-height: 22px; color: #333; }
  .btn-more {
    left: 380px; top: 583px; width: 149px; height: 43px; border-radius: 4px;
    background: linear-gradient(#b6dcf6, #6aaee0);
    font-family: "PT Sans", sans-serif; font-size: 16px; color: #112; display: flex; align-items: center; justify-content: center;
  }
  .btn-reflection { left: 380px; top: 628px; width: 149px; height: 30px; border-radius: 4px 4px 0 0;
    background: linear-gradient(rgba(106,174,224,0.55), rgba(255,255,255,0)); }

  .picks { left: 27px; top: 690px; width: 580px; height: 183px; }
  .thumb { top: 742px; width: 119px; height: 101px; border: 2px solid #9eb3c5; padding: 3px; background: var(--white);
    box-shadow: 0 1px 3px rgba(0,0,0,0.25); }
  .thumb-fill { width: 100%; height: 100%; border: 2px solid #2f5c86; }

  .news { left: 27px; top: 890px; width: 580px; height: 184px; }
  .news-divider { left: 315px; top: 911px; width: 1px; height: 153px; background: #cccccc; }
  .date-badge { width: 44px; height: 44px; border-radius: 3px; background: linear-gradient(#5aa6e0, var(--badge-blue));
    color: var(--white); font-size: 11px; font-weight: 700; text-align: center; line-height: 14px; padding-top: 8px; }
  .news-text { font-size: 11px; line-height: 16px; color: var(--ink-soft); width: 180px; }
  .blog-icon { width: 50px; height: 52px; border-radius: 6px; background: linear-gradient(135deg, #3d8ed2, #f39a1a); }
  .blog-date { font-size: 11px; color: var(--link-blue); }

  .login { left: 637px; top: 552px; width: 246px; height: 215px; }
  .side-bar {
    left: 644px; width: 231px; height: 38px; border-radius: 4px;
    background: linear-gradient(var(--bar-top), var(--bar-bottom));
    font-family: "PT Sans", sans-serif; font-size: 15px; padding: 9px 0 0 14px; color: #112;
  }
  .field-label { left: 667px; font-size: 12px; color: var(--ink); }
  .field { left: 667px; width: 145px; height: 23px; background: var(--field-bg); border: 1px solid var(--field-line); }
  .btn-login { left: 667px; top: 726px; width: 57px; height: 24px; border: 1px solid #aaaaaa; border-radius: 2px;
    background: linear-gradient(#ffffff, #e4e4e4); font-size: 11px; color: #a0203a; display: flex; align-items: center; justify-content: center; }

  .categories { left: 637px; top: 785px; width: 246px; height: 161px; }
  .cat-item { left: 660px; font-family: "PT Sans", sans-serif; font-size: 13px; color: #333; display: flex; align-items: center; gap: 7px; }
  .cat-item svg { flex: none; }

  .social { left: 637px; top: 962px; width: 246px; height: 115px; }
  .social-heading { left: 660px; top: 974px; }
  .social-square { top: 1013px; width: 29px; height: 29px; border-radius: 4px; }

  /* footer */
  .skyline { left: 0; top: 1076px; width: 905px; height: 124px;
    background: linear-gradient(180deg, #f2f2f2 0%, #d8d8d8 100%); }
  .footer-bar { left: 15px; top: 1120px; width: 873px; height: 65px;
    background: linear-gradient(#8cc3ec 0%, #e8f4fc 70%, #ffffff 100%); border-radius: 2px; }
  .footer-links { left: 0; width: 905px; top: 1135px; text-align: center; font-family: "PT Sans", sans-serif; font-size: 12px; color: #111; word-spacing: 4px; }
  .footer-links span { margin: 0 8px; }
  .copyright { left: 0; width: 905px; top: 1159px; text-align: center; font-size: 11px; color: #333; }
</style>
</head>
<body>

<header>
  <div class="abs sky" role="img" aria-label="Bright blue sky with white clouds"></div>
  <div class="abs brand">
    <span class="brand-mark"></span>
    <span class="brand-name">tavernik</span>
  </div>
  <p class="abs tagline">Locate, Explore and Discover the best of your city with tavernik</p>
  <nav>
    <a class="abs nav nav-home">Home</a>
    <a class="abs nav nav-about">About Us</a>
    <a class="abs nav nav-contact">Contact Us</a>
  </nav>
</header>

<section>
  <div class="abs slider"></div>
  <div class="abs slide slide-beauty">
    <div class="slide-photo" role="img" aria-label="Couple wading in a turquoise lagoon with rocky islands">
      <span class="slide-title">Beauty Places</span>
      <span class="slide-cta">Join for free today!</span>
    </div>
  </div>
  <div class="abs slide slide-food">
    <div class="slide-photo" role="img" aria-label="Plated dessert with cheesecake and small doughnuts on a sauce swirl">
      <span class="slide-title">Food and Hotels</span>
      <span class="slide-cta">Join for free today!</span>
    </div>
  </div>
  <div class="abs slide slide-theatre">
    <div class="slide-photo" role="img" aria-label="Theatre hall with red seats facing a lit stage">
      <span class="slide-title">Theatres</span>
      <span class="slide-cta">Join for free today!</span>
    </div>
  </div>
  <div class="abs slider-arrow arrow-left">
    <svg width="14" height="14" viewBox="0 0 14 14"><path d="M1 2l5 5-5 5M7 2l5 5-5 5" fill="none" stroke="#222" stroke-width="2.4"/></svg>
  </div>
  <div class="abs slider-arrow arrow-right">
    <svg width="14" height="14" viewBox="0 0 14 14"><path d="M13 2L8 7l5 5M7 2L2 7l5 5" fill="none" stroke="#222" stroke-width="2.4"/></svg>
  </div>
</section>

<main>
  <div class="abs box intro"></div>
  <p class="abs intro-copy">Discover your cities hottest offers<br>places &amp; venues while sharing<br>the things that mean the most to you.</p>
  <div class="abs btn-reflection"></div>
  <a class="abs btn-more">VIEW MORE</a>

  <div class="abs box picks"></div>
  <h2 class="abs box-heading" style="left:48px;top:703px;">Top Picks</h2>
  <div class="abs thumb" style="left:49px;"><div class="thumb-fill" role="img" aria-label="Beach huts by palm trees" style="background:linear-gradient(#4aa0e0,#bfe4f2 60%,#e8e0c0);"></div></div>
  <div class="abs thumb" style="left:186px;"><div class="thumb-fill" role="img" aria-label="Steak on a flaming grill" style="background:linear-gradient(#3a2418,#c2562a 50%,#6a3a24);"></div></div>
  <div class="abs thumb" style="left:322px;"><div class="thumb-fill" role="img" aria-label="Houseboat on a green backwater" style="background:linear-gradient(#9cc6e6,#4d7a3a 45%,#6e8a6a);"></div></div>
  <div class="abs thumb" style="left:459px;"><div class="thumb-fill" role="img" aria-label="Lakeside table set for a meal" style="background:linear-gradient(#c8d8e8,#7a96b0 50%,#3a4a5a);"></div></div>
  <a class="abs link-more" style="left:521px;top:856px;">VIEW MORE</a>

  <div class="abs box news"></div>
  <h2 class="abs box-heading" style="left:50px;top:908px;">Latest News</h2>
  <div class="abs date-badge" style="left:52px;top:946px;">NOV 29<br>2011</div>
  <p class="abs news-text" style="left:119px;top:943px;">Lorem Ipsum is simply dummy text of the printing and typesetting industry</p>
  <div class="abs date-badge" style="left:52px;top:1006px;">NOV 29<br>2011</div>
  <p class="abs news-text" style="left:118px;top:1006px;">Lorem Ipsum is simply dummy text of the printing and typesetting industry.</p>
  <a class="abs link-more" style="left:233px;top:1052px;">VIEW MORE</a>
  <div class="abs news-divider"></div>

  <h2 class="abs box-heading" style="left:349px;top:908px;">Blog</h2>
  <div class="abs blog-icon" role="img" aria-label="Blog post icon" style="left:347px;top:937px;"></div>
  <p class="abs blog-date" style="left:417px;top:928px;">NOV 29, 2011</p>
  <p class="abs news-text" style="left:417px;top:943px;">Lorem Ipsum is simply dummy text of the printing and typesetting industry.</p>
  <div class="abs blog-icon" role="img" aria-label="Blog post icon" style="left:347px;top:1010px;"></div>
  <p class="abs blog-date" style="left:417px;top:1001px;">NOV 29, 2011</p>
  <p class="abs news-text" style="left:417px;top:1016px;">Lorem Ipsum is simply dummy text of the printing and typesetting industry.</p>
</main>

<aside>
  <div class="abs box login"></div>
  <div class="abs side-bar" style="top:557px;">MEMBERS LOGIN</div>
  <label class="abs field-label" style="top:610px;">Username</label>
  <div class="abs field" style="top:628px;"></div>
  <label class="abs field-label" style="top:657px;">Password</label>
  <div class="abs field" style="top:675px;"></div>
  <label class="abs field-label" style="top:704px;">Remember me</label>
  <svg class="abs" style="left:747px;top:703px;" width="13" height="13" viewBox="0 0 13 13">
    <rect x="0.5" y="0.5" width="12" height="12" fill="#fff" stroke="#666"/>
    <path d="M3 6.5l2.5 2.5L10 3.5" fill="none" stroke="#1a8a3a" stroke-width="1.8"/>
  </svg>
  <a class="abs btn-login">Login</a>

  <div class="abs box categories"></div>
  <div class="abs side-bar" style="top:792px;">CATEGORIES</div>
  <div class="abs cat-item" style="top:851px;"><svg width="11" height="12" viewBox="0 0 11 12"><path d="M0 0l11 6-11 6z" fill="#5a86b4"/></svg>Fashion &amp; Beauty</div>
  <div class="abs cat-item" style="top:881px;"><svg width="11" height="12" viewBox="0 0 11 12"><path d="M0 0l11 6-11 6z" fill="#5a86b4"/></svg>Food &amp; Drink</div>
  <div class="abs cat-item" style="top:911px;"><svg width="11" height="12" viewBox="0 0 11 12"><path d="M0 0l11 6-11 6z" fill="#5a86b4"/></svg>Entertainment &amp; Events</div>

  <div class="abs box social"></div>
  <h2 class="abs box-heading social-heading">STAY WITH US</h2>
  <span class="abs social-square" style="left:658px;background:#2a5aa8;"></span>
  <span class="abs social-square" style="left:690px;background:#3bb0e0;"></span>
  <span class="abs social-square" style="left:723px;background:#1f6aa8;"></span>
  <span class="abs social-square" style="left:755px;background:#f08a24;"></span>
</aside>

<footer>
  <div class="abs skyline" role="img" aria-label="Faint grey city skyline"></div>
  <div class="abs footer-bar"></div>
  <p class="abs footer-links">Home<span>|</span>About Us<span>|</span>Sitemap<span>|</span>Contact Us</p>
  <p class="abs copyright">Copyright ©&nbsp; Halden, All Rights Reserved</p>
</footer>

</body>
</html>
```